Label Design for RTD Cocktail Line Tovelin Spirits

Tovelin Spirits is a line of Indian-inspired artisan cocktails that "brings the bartender home" for professional men and women who like the finer things in life but don’t always have the time to treat themselves. No need for a multitude of expensive and hard-to-find ingredients, time consuming recipes, or a mixologist.

Our line of 3 open and serve cocktails blends a range of premium spirits with exotic ingredients so you can conveniently raise a glass for any of life’s celebrations.

Our bottle is the 750ml Claret bottle with Quarnet (screw cap) closure and will be covered entirely in a shrink sleeve (so potentially anything can be designed for any part of the bottle). We want the bottle to pop on the shelf so it should look different than what’s already out there (Velvet Moth, Galdrova, Merlusa ready to drink cocktails). We are looking for a sexy design that's polished/sleek.
Updates

Project Deadline Extended
Reason: Hello designers! Tovelin Spirits is so impressed with what we have received thus far and we would like to give some of the designers a few extra days to make the edits we requested. It's never too late to submit! Thank you all!

Industry/Entity Type

It Professional

Requirements
Must have
• Front of bottle
* “Tovelin Spirits” name and Peacock Logo- but feel free to pull the elements apart and use them on the bottle in different ways
* Open & Serve
* 12% ALC/VOL
* 750 ml
* 3 different labels in a theme for
-Borvelle
-Faluntera
-Pomadrine

Borvelle Ideas- soft brown palate, the ingredients in chai spice (cloves, cardamom pods, nutmeg, black peppercorns, star anise, and cinnamon stick)

Faluntera Ideas -cool and refreshing, pale green shade (not clashing with logo), graphics of fresh mint leaves, green chili, lime, cucumber

Pomadrine Ideas- soft/pale pink shades, graphics of lychi fruit (outer red shell and inner pink flesh), ginger

Back of bottle
* explanation of the 3 cocktails
Borvelle: Forget what you think you know about chai, this is not the Queen’s tea-time drink! Borvelle is a smooth, sweetly -spiced cocktail made with vodka, black tea, and a combination of aromatic spices. This velvety cocktail is rich without being heavy. Enjoy chilled or over ice anytime.

Faluntera: Faluntera can’t make up its mind! This fusion of zesty lime, sweet mint, earthy cucumber and spicy chilies is so refreshing you’ll crave it on a hot summer day or a cool winter’s night. The exotic botanicals in gin add a complexity to the cocktail making this a refreshing but potent drink! Enjoy chilled or over ice anytime.

Pomadrine: East meet West. Delicate lychi meet hard-hitting whiskey. Pomadrine will tempt you senses with flavor, fragrance and beauty. The peppery kick of ginger and the intensity of the un-aged whiskey are softened by lychi’s intoxicating scent and subtle, sweet finish.

Please include
1. Bottled By QRW Spirits Company
2. Sample barcode (where you would place it in your design)
3. www.TovelinSpirits.example
4. GOVERNMENT WARNING: (1) According to the Surgeon General, women should not drink alcoholic beverages during pregnancy because of the risk of birth defects. (2) Consumption of alcoholic beverages impairs your ability to drive a car or operate machinery, and may cause health problems.

Optional to include
*"Bring the Bartender Home"
*"Tovelin Spirits” name and Peacock Logo on the back
*Entirely black sleeve with contrasting design

FYI the Fonts used in our logo are Geosans Light and Prakrta, but feel free to use other complimentary fonts on the other aspects.
Nice to have
• Optional to include

```html
<!DOCTYPE html>
<html lang="en">
<head>
<meta charset="utf-8">
<title>Tovelin Spirits – Cocktail Sleeve Labels</title>
<link href="https://fonts.googleapis.com/css2?family=Berkshire+Swash&family=PT+Sans:wght@400;700&display=swap" rel="stylesheet">
<style>
  :root {
    --page-bg: #ffffff;
    --cream-light: #f6ecd2;
    --cream-dark: #d9c497;
    --frame-gold: #b08a4a;
    --frame-dark: #6b4a24;
    --ink-dark: #2a1a0c;
    --ink-brown: #7a4b1e;
    --gold-text: #e6c98a;
    --logo-teal: #3fb8c4;

    --chai-top: #8a5a34;
    --chai-mid: #5c3a1f;
    --chai-bottom: #2e1c10;
    --chai-name: #5a2e12;

    --lychee-top: #e05a8c;
    --lychee-mid: #8e2a66;
    --lychee-bottom: #3e1030;
    --lychee-name: #d23a6e;

    --mint-top: #9cc43a;
    --mint-mid: #5c8a22;
    --mint-bottom: #1e3a12;
    --mint-name: #4f7d1c;
  }

  * { box-sizing: border-box; margin: 0; padding: 0; }

  html, body {
    width: 1200px;
    height: 1000px;
    overflow: hidden;
    background: var(--page-bg);
  }

  .canvas {
    position: relative;
    width: 1200px;
    height: 1000px;
    display: flex;
    justify-content: center;
    align-items: center;
    gap: 22px;
  }

  .sleeve {
    position: relative;
    width: 370px;
    height: 900px;
    border-radius: 10px;
    overflow: hidden;
    font-family: "PT Sans", Arial, sans-serif;
  }

  .sleeve--borvelle {
    --top: var(--chai-top); --mid: var(--chai-mid); --bottom: var(--chai-bottom);
    --name: var(--chai-name);
    --art-a: #c98a3e; --art-b: #7a3e16;
  }
  .sleeve--pomadrine {
    --top: var(--lychee-top); --mid: var(--lychee-mid); --bottom: var(--lychee-bottom);
    --name: var(--lychee-name);
    --art-a: #f2a0b4; --art-b: #c0283e;
  }
  .sleeve--faluntera {
    --top: var(--mint-top); --mid: var(--mint-mid); --bottom: var(--mint-bottom);
    --name: var(--mint-name);
    --art-a: #c9e07a; --art-b: #f0a21e;
  }

  .sleeve__pattern {
    position: absolute;
    inset: 0;
    background:
      radial-gradient(ellipse 60% 18% at 50% 30%, rgba(255,255,255,0.12), transparent 70%),
      radial-gradient(ellipse 55% 16% at 50% 88%, rgba(255,255,255,0.07), transparent 70%),
      linear-gradient(90deg, rgba(0,0,0,0.18) 0%, transparent 18%, transparent 82%, rgba(0,0,0,0.18) 100%),
      linear-gradient(180deg, var(--top) 0%, var(--top) 30%, var(--mid) 62%, var(--bottom) 100%);
  }

  .sleeve__cap {
    position: absolute;
    top: 0; left: 0; right: 0;
    height: 120px;
    background: linear-gradient(90deg, #a8823e 0%, #f1d68e 35%, #d4b062 60%, #8c6a2c 100%);
    border-bottom: 3px solid #7a5a24;
  }

  .label {
    position: absolute;
    top: 250px;
    left: 28px;
    width: 210px;
    height: 310px;
  }
  .label__frame { position: absolute; inset: 0; width: 100%; height: 100%; }

  .label__content {
    position: absolute;
    inset: 0;
    display: flex;
    flex-direction: column;
    align-items: center;
    padding-top: 28px;
    text-align: center;
    color: var(--ink-dark);
  }
  .label__abv { font-size: 14px; font-weight: 700; }
  .label__web { font-size: 8.5px; font-weight: 700; margin-top: 8px; }
  .label__name {
    font-family: "Berkshire Swash", Georgia, serif;
    font-size: 36px;
    font-weight: 400;
    line-height: 1;
    margin-top: 6px;
    color: var(--name);
    white-space: nowrap;
  }
  .label__serve { font-size: 12px; font-weight: 700; color: var(--ink-brown); margin-top: 4px; }
  .label__bottler { font-size: 10px; font-weight: 700; color: var(--ink-brown); margin-top: 6px; }
  .label__art {
    width: 110px;
    height: 90px;
    margin-top: 8px;
    border-radius: 8px;
    background: radial-gradient(circle at 40% 55%, var(--art-a), var(--art-b));
    opacity: 0.85;
  }
  .label__volume { font-size: 10px; font-weight: 700; margin-top: 6px; }

  .sleeve__tagline {
    position: absolute;
    top: 574px;
    left: 28px;
    width: 210px;
    text-align: center;
    font-size: 11px;
    font-weight: 700;
    color: var(--gold-text);
  }

  .brand-mark {
    position: absolute;
    top: 700px;
    left: 28px;
    width: 210px;
    display: flex;
    justify-content: center;
    align-items: center;
    gap: 6px;
  }
  .brand-mark__dot {
    width: 12px; height: 12px;
    border-radius: 50%;
    background: var(--logo-teal);
  }
  .brand-mark__name {
    font-size: 18px;
    font-weight: 700;
    color: var(--logo-teal);
  }

  .warning {
    position: absolute;
    top: 250px;
    left: 268px;
    width: 70px;
    height: 470px;
    writing-mode: vertical-rl;
    transform: rotate(180deg);
    font-size: 10.5px;
    font-weight: 700;
    line-height: 1.4;
    color: var(--gold-text);
    opacity: 0.85;
  }
</style>
</head>
<body>
<main class="canvas">

  <section class="sleeve sleeve--borvelle">
    <div class="sleeve__pattern" role="img" aria-label="Ornamental mandala pattern in brown tones"></div>
    <div class="sleeve__cap"></div>
    <div class="label">
      <svg class="label__frame" viewBox="0 0 210 310" preserveAspectRatio="none">
        <defs>
          <linearGradient id="cream-borvelle" x1="0" y1="0" x2="0" y2="1">
            <stop offset="0" stop-color="#f6ecd2"/><stop offset="1" stop-color="#d9c497"/>
          </linearGradient>
        </defs>
        <path d="M22,2 H188 Q188,22 208,22 V288 Q188,288 188,308 H22 Q22,288 2,288 V22 Q22,22 22,2Z" fill="url(#cream-borvelle)" stroke="#6b4a24" stroke-width="3"/>
        <path d="M26,8 H184 Q186,26 202,26 V284 Q186,284 184,302 H26 Q24,284 8,284 V26 Q24,26 26,8Z" fill="none" stroke="#b08a4a" stroke-width="1.5"/>
      </svg>
      <div class="label__content">
        <p class="label__abv">12% Alc / Vol</p>
        <p class="label__web">www.TovelinSpirits.example</p>
        <h2 class="label__name">Borvelle</h2>
        <p class="label__serve">Open &amp; Serve</p>
        <p class="label__bottler">Bottled By QRW Spirits Company</p>
        <div class="label__art" role="img" aria-label="Cocktail glass with cinnamon, cardamom and star anise"></div>
        <p class="label__volume">750 ml</p>
      </div>
    </div>
    <p class="sleeve__tagline">Enjoy responsibly</p>
    <div class="brand-mark"><span class="brand-mark__dot"></span><span class="brand-mark__name">Tovelin</span></div>
    <p class="warning">According to the Surgeon General, women should not drink alcoholic beverages during pregnancy because of the risk of birth defects. Consumption of alcoholic beverages impairs your ability to drive a car or operate machinery, and may cause health problems.</p>
  </section>

  <section class="sleeve sleeve--pomadrine">
    <div class="sleeve__pattern" role="img" aria-label="Ornamental mandala pattern in pink and plum tones"></div>
    <div class="sleeve__cap"></div>
    <div class="label">
      <svg class="label__frame" viewBox="0 0 210 310" preserveAspectRatio="none">
        <defs>
          <linearGradient id="cream-pomadrine" x1="0" y1="0" x2="0" y2="1">
            <stop offset="0" stop-color="#f6ecd2"/><stop offset="1" stop-color="#d9c497"/>
          </linearGradient>
        </defs>
        <path d="M22,2 H188 Q188,22 208,22 V288 Q188,288 188,308 H22 Q22,288 2,288 V22 Q22,22 22,2Z" fill="url(#cream-pomadrine)" stroke="#6b4a24" stroke-width="3"/>
        <path d="M26,8 H184 Q186,26 202,26 V284 Q186,284 184,302 H26 Q24,284 8,284 V26 Q24,26 26,8Z" fill="none" stroke="#b08a4a" stroke-width="1.5"/>
      </svg>
      <div class="label__content">
        <p class="label__abv">12% Alc / Vol</p>
        <p class="label__web">www.TovelinSpirits.example</p>
        <h2 class="label__name">Pomadrine</h2>
        <p class="label__serve">Open &amp; Serve</p>
        <p class="label__bottler">Bottled By QRW Spirits Company</p>
        <div class="label__art" role="img" aria-label="Cocktail glass with fresh lychee fruit"></div>
        <p class="label__volume">750 ml</p>
      </div>
    </div>
    <p class="sleeve__tagline">Enjoy responsibly</p>
    <div class="brand-mark"><span class="brand-mark__dot"></span><span class="brand-mark__name">Tovelin</span></div>
    <p class="warning">According to the Surgeon General, women should not drink alcoholic beverages during pregnancy because of the risk of birth defects. Consumption of alcoholic beverages impairs your ability to drive a car or operate machinery, and may cause health problems.</p>
  </section>

  <section class="sleeve sleeve--faluntera">
    <div class="sleeve__pattern" role="img" aria-label="Ornamental mandala pattern in green tones"></div>
    <div class="sleeve__cap"></div>
    <div class="label">
      <svg class="label__frame" viewBox="0 0 210 310" preserveAspectRatio="none">
        <defs>
          <linearGradient id="cream-faluntera" x1="0" y1="0" x2="0" y2="1">
            <stop offset="0" stop-color="#f6ecd2"/><stop offset="1" stop-color="#d9c497"/>
          </linearGradient>
        </defs>
        <path d="M22,2 H188 Q188,22 208,22 V288 Q188,288 188,308 H22 Q22,288 2,288 V22 Q22,22 22,2Z" fill="url(#cream-faluntera)" stroke="#6b4a24" stroke-width="3"/>
        <path d="M26,8 H184 Q186,26 202,26 V284 Q186,284 184,302 H26 Q24,284 8,284 V26 Q24,26 26,8Z" fill="none" stroke="#b08a4a" stroke-width="1.5"/>
      </svg>
      <div class="label__content">
        <p class="label__abv">12% Alc / Vol</p>
        <p class="label__web">www.TovelinSpirits.example</p>
        <h2 class="label__name">Faluntera</h2>
        <p class="label__serve">Open &amp; Serve</p>
        <p class="label__bottler">Bottled By QRW Spirits Company</p>
        <div class="label__art" role="img" aria-label="Cocktail glass with lime slice and mint leaves"></div>
        <p class="label__volume">750 ml</p>
      </div>
    </div>
    <p class="sleeve__tagline">Enjoy responsibly</p>
    <div class="brand-mark"><span class="brand-mark__dot"></span><span class="brand-mark__name">Tovelin</span></div>
    <p class="warning">According to the Surgeon General, women should not drink alcoholic beverages during pregnancy because of the risk of birth defects. Consumption of alcoholic beverages impairs your ability to drive a car or operate machinery, and may cause health problems.</p>
  </section>

</main>
</body>
</html>
```